LantrovaMD Biz Card

We need a business card design for a software firm servicing the medical arena. This will be a plastic card, translucent. I will upload our site beta for layout ideas. We will be utilizing clear/plastic business cards for printing.

Target Market(s)

Medical Providers

Industry/Entity Type

Information Technology

Contact Information for Business Card

Kurt Basford
Managing Director

4738 Hollis Creek Drive
Suite 300
Brookvale, SC 30857
kbasford@LantrovaMD.example
(877)555-0193 Toll Free
(706)555-0148 Mobile

Font styles to use
Serif
Sans Serif

Colors
0592cd
00a990
33b8a4
33a6d7

```html
<!DOCTYPE html>
<html lang="en">
<head>
<meta charset="utf-8">
<title>LantrovaMD Business Card</title>
<link rel="stylesheet" href="https://fonts.googleapis.com/css2?family=Arimo:wght@400;700&display=swap">
<style>
  :root {
    --page-bg: #e9ebee;
    --card-bg: #ffffff;
    --brand-green: #7cc243;
    --brand-blue: #1f5b8e;
    --brand-blue-mid: #2e6da3;
    --text-blue: #2a5f93;
    --shadow: rgba(20, 30, 45, 0.18);
  }
  * { box-sizing: border-box; margin: 0; padding: 0; }
  html, body {
    width: 1200px;
    height: 997px;
    overflow: hidden;
    background: var(--page-bg);
  }
  .stage {
    position: relative;
    width: 1200px;
    height: 997px;
  }
  .card {
    position: absolute;
    left: 240px;
    width: 720px;
    height: 412px;
    background: var(--card-bg);
    border-radius: 22px;
    box-shadow: 0 10px 30px var(--shadow);
    overflow: hidden;
  }
  .card--front { top: 52px; }
  .card--back { top: 533px; }

  /* brand name */
  .brand {
    position: absolute;
    left: 0;
    right: 0;
    display: flex;
    justify-content: center;
    align-items: center;
    gap: 14px;
    font-family: "Arimo", sans-serif;
    font-weight: 400;
    color: var(--brand-blue);
  }
  .card--front .brand { top: 170px; font-size: 52px; }
  .card--back .brand { top: 50px; font-size: 42px; }
  .brand__dot {
    border-radius: 50%;
    background: var(--brand-blue);
  }
  .card--front .brand__dot { width: 26px; height: 26px; }
  .card--back .brand__dot { width: 22px; height: 22px; }

  /* contact details */
  .contact {
    position: absolute;
    right: 78px;
    top: 150px;
    text-align: right;
    font-family: "Arimo", sans-serif;
    font-style: normal;
    font-size: 17px;
    line-height: 24px;
    color: var(--text-blue);
  }
  .contact__gap { height: 8px; }
  .icon-tab {
    position: absolute;
    right: 0;
    top: 140px;
    width: 44px;
    height: 112px;
    background: var(--brand-blue-mid);
    border-radius: 10px 0 0 10px;
    display: flex;
    flex-direction: column;
    align-items: center;
    justify-content: space-around;
    padding: 10px 0;
  }
  .icon-tab svg { width: 16px; height: 16px; }

  .person {
    position: absolute;
    left: 42px;
    top: 222px;
    font-family: "Arimo", sans-serif;
    color: var(--text-blue);
    font-size: 17px;
    line-height: 24px;
  }
  .person__name {
    font-weight: 700;
    font-size: 20px;
    color: var(--brand-green);
    text-transform: uppercase;
  }

  /* bottom bands */
  .rule-green {
    position: absolute;
    left: 0; right: 0;
    height: 3px;
    background: var(--brand-green);
  }
  .rule-green--top { top: 306px; }
  .rule-green--bottom { top: 400px; }
  .web-band {
    position: absolute;
    left: 0; right: 0;
    top: 314px;
    height: 42px;
    background: var(--brand-blue);
    display: flex;
    align-items: center;
    justify-content: center;
    font-family: "Arimo", sans-serif;
    font-weight: 700;
    font-size: 17px;
    letter-spacing: 2px;
    color: #ffffff;
  }
  .base-band {
    position: absolute;
    left: 0; right: 0;
    top: 366px;
    height: 30px;
    background: var(--brand-blue);
  }
</style>
</head>
<body>
<main class="stage">

  <section class="card card--front" aria-label="Card front">
    <div class="brand"><span class="brand__dot"></span>LantrovaMD</div>
  </section>

  <section class="card card--back" aria-label="Card back">
    <div class="brand"><span class="brand__dot"></span>LantrovaMD</div>

    <address class="contact">
      <div>(877) 555-0193</div>
      <div>(706) 555-0148</div>
      <div class="contact__gap"></div>
      <div>4738 Hollis Creek Drive, Suite 300</div>
      <div>Brookvale, SC 30857</div>
    </address>

    <div class="icon-tab" aria-hidden="true">
      <svg viewBox="0 0 16 16"><path fill="#7cc243" d="M3 2h3l1.5 3.5-2 1.2a8 8 0 0 0 3.8 3.8l1.2-2L14 10v3a1 1 0 0 1-1 1A11 11 0 0 1 2 3a1 1 0 0 1 1-1z"/></svg>
      <svg viewBox="0 0 16 16"><rect x="4" y="1" width="8" height="14" rx="1.5" fill="#7cc243"/><rect x="5.5" y="3" width="5" height="8" fill="#2e6da3"/></svg>
      <svg viewBox="0 0 16 16"><path fill="#7cc243" d="M8 1a5 5 0 0 1 5 5c0 4-5 9-5 9S3 10 3 6a5 5 0 0 1 5-5z"/><circle cx="8" cy="6" r="2" fill="#2e6da3"/></svg>
    </div>

    <div class="person">
      <div class="person__name">Kurt Basford</div>
      <div>Managing Director</div>
      <div>kbasford@LantrovaMD.example</div>
    </div>

    <div class="rule-green rule-green--top"></div>
    <div class="web-band">www.lantrovaMD.example</div>
    <div class="base-band"></div>
    <div class="rule-green rule-green--bottom"></div>
  </section>

</main>
</body>
</html>
```